Business Card for Professional Photographer

I'm looking for an eye catching modern clean design that compliments my logo/ website fonts & colours.
I specialise in architecture, corporate & commercial photography so I'm marketing to professional clients rather than portrait / wedding clients.

I would prefer to not have a solid black design.

My logo brand guide is as follows :

Main front font. : Reislust
Main font colour : #fff
Slogan front font : Ubuntu Bold
Monogram front font : Venti Medium
Container colour : #fff

I need print ready files in pdf .png & .eps formats.

Included in the files below are some screen grabs as reference to font & colours etc.

```html
<!DOCTYPE html>
<html lang="en">
<head>
<meta charset="utf-8">
<title>Turning Light – Business Card</title>
<link rel="stylesheet" href="https://fonts.googleapis.com/css2?family=Montserrat:wght@700&family=Open+Sans:wght@400;600&display=swap">
<style>
  :root {
    --bg: #2b2b2c;
    --card: #0e0e0f;
    --gold: #d9b24a;
    --gold-light: #f3d77e;
    --gold-dark: #9c7a26;
    --white: #ffffff;
    --muted: #cfcfcf;
    --rule: #2f2f31;
  }
  * { margin: 0; padding: 0; box-sizing: border-box; }
  html, body { width: 1200px; height: 866px; overflow: hidden; }
  body {
    background: var(--bg);
    font-family: "Open Sans", sans-serif;
    color: var(--white);
    display: flex;
    flex-direction: column;
    align-items: center;
    justify-content: center;
    gap: 40px;
  }
  .card {
    position: relative;
    width: 640px;
    height: 366px;
    background: var(--card);
    overflow: hidden;
    box-shadow: 0 14px 30px rgba(0,0,0,.55);
  }
  .card::after {
    content: "";
    position: absolute;
    left: 0; right: 0; bottom: 0;
    height: 7px;
    background: linear-gradient(90deg, var(--gold-dark), var(--gold-light) 35%, var(--gold) 65%, var(--gold-light));
  }
  .collage {
    position: absolute;
    inset: 0;
    background:
      linear-gradient(rgba(10,10,12,.55), rgba(10,10,12,.55)),
      linear-gradient(115deg, #1d2b3a 0%, #3b3f44 28%, #6b5a44 45%, #3a3630 62%, #2c3946 80%, #50565c 100%);
  }
  .brand { position: absolute; }
  .brand-name {
    font-family: "Open Sans", sans-serif;
    font-weight: 400;
    font-size: 28px;
    letter-spacing: 5px;
    color: var(--white);
    line-height: 1;
    white-space: nowrap;
  }
  .brand-tagline {
    font-size: 9.5px;
    letter-spacing: 2.6px;
    color: var(--muted);
    margin-top: 7px;
    white-space: nowrap;
  }
  .card-front .brand { left: 50%; top: 150px; transform: translateX(-50%); text-align: center; }

  .card-back .brand { right: 40px; top: 100px; text-align: right; }
  .card-back .brand-name { font-size: 24px; letter-spacing: 4px; }
  .contact { position: absolute; left: 40px; top: 80px; }
  .person-name {
    font-family: "Montserrat", sans-serif;
    font-weight: 700;
    font-size: 21px;
    letter-spacing: 1px;
    color: var(--gold);
    text-transform: uppercase;
  }
  .person-role { font-size: 15px; margin: 2px 0 12px; }
  .contact-list { list-style: none; font-size: 14px; line-height: 1.6; }
  .contact-list li { display: flex; align-items: center; gap: 8px; }
  .contact-list svg { width: 13px; height: 13px; fill: var(--gold); flex: none; }
  .divider {
    position: absolute;
    left: 40px; right: 40px; top: 226px;
    height: 1px;
    background: var(--rule);
  }
  .address {
    position: absolute;
    right: 40px;
    top: 246px;
    font-size: 15px;
    font-style: normal;
    line-height: 1.45;
    letter-spacing: .5px;
    text-align: right;
  }
</style>
</head>
<body>

  <section class="card card-front">
    <div class="collage" role="img" aria-label="Collage of architecture, interior and product photographs in muted blue and warm tones"></div>
    <div class="brand">
      <div class="brand-name">TURNING LIGHT</div>
      <div class="brand-tagline">Buildings Brands Business</div>
    </div>
  </section>

  <section class="card card-back">
    <div class="contact">
      <div class="person-name">Daniel Marsh</div>
      <div class="person-role">Managing Director</div>
      <ul class="contact-list">
        <li><svg viewBox="0 0 16 16"><path d="M3 1h3l1.5 4-2 1.3a9 9 0 0 0 4.2 4.2L11 8.5l4 1.5v3a2 2 0 0 1-2 2A12 12 0 0 1 1 3a2 2 0 0 1 2-2z"/></svg>044-555 010 222</li>
        <li><svg viewBox="0 0 16 16"><path d="M1 3h14v10H1z M1.5 3.5 8 9l6.5-5.5" fill="none" stroke="#d9b24a" stroke-width="1.6"/></svg>hello@turninglight.com</li>
        <li><svg viewBox="0 0 16 16"><circle cx="8" cy="8" r="7"/><circle cx="8" cy="8" r="2.5" fill="#0e0e0f"/></svg>www.turninglight.com</li>
      </ul>
    </div>
    <div class="brand">
      <div class="brand-name">TURNING LIGHT</div>
      <div class="brand-tagline">Buildings Brands Business</div>
    </div>
    <div class="divider"></div>
    <address class="address">48, Harbour Lane Studios<br>Northbridge, 204118</address>
  </section>

</body>
</html>
```